Indy Film Production Company/Studio

We need a business card designed from an existing logo. We are a digital studio/production company that caters to creating genre entertainment, like Action, Horror, and martial arts. The card along with the logo will be used to Brand the company from letter heads to banners. The design will also be used for postcards and Brochures. It should be professional and masculine.
Updates

Thank you to all the designers who have participated. I'm narrowing down who it will be. Thank you again.

Target Market(s)

Investors, Networks, Producers, and actors

Industry/Entity Type

Film Production

Contact Information for Business Card

Benedikt Harwell
Producer/Writer/Director
www.copperlatchpictures.com

Requirements
Must have
• Website address, Friendloop icon and Chirper icon possibly in the back of the card.
Nice to have
• Logline of Company: Follow The Action.

```html
<!DOCTYPE html>
<html lang="en">
<head>
<meta charset="utf-8">
<title>Copperlatch Pictures – Business Card</title>
<link rel="stylesheet" href="https://fonts.googleapis.com/css2?family=PT+Sans:wght@400;700&display=swap">
<style>
  :root {
    --stage: #3b3b3b;
    --brand-red: #e31b23;
    --paper: #f7f7f7;
    --ink: #1e1e1e;
    --muted: #555555;
    --rule: #b9b9b9;
    --white: #ffffff;
  }
  * { box-sizing: border-box; margin: 0; padding: 0; }
  html, body {
    width: 1200px; height: 750px; overflow: hidden;
    background: var(--stage);
    font-family: "PT Sans", sans-serif;
  }
  .canvas { position: relative; width: 1200px; height: 750px; }

  .card {
    position: absolute; left: 371px; width: 461px; height: 263px;
    box-shadow: 0 4px 10px rgba(0,0,0,0.45);
  }
  .card--front { top: 81px; background: var(--paper); }
  .card--back { top: 382px; background: var(--brand-red); }

  .crop-mark { position: absolute; width: 23px; height: 23px; border-color: var(--brand-red); border-style: solid; border-width: 0; }
  .card--back .crop-mark { border-color: var(--white); }
  .crop-mark--tl { top: 10px; left: 10px; border-top-width: 2px; border-left-width: 2px; }
  .crop-mark--tr { top: 10px; right: 10px; border-top-width: 2px; border-right-width: 2px; }
  .crop-mark--bl { bottom: 10px; left: 10px; border-bottom-width: 2px; border-left-width: 2px; }
  .crop-mark--br { bottom: 10px; right: 10px; border-bottom-width: 2px; border-right-width: 2px; }

  .wordmark {
    position: absolute; font-weight: 700; text-transform: uppercase;
    line-height: 1.02; letter-spacing: 0.5px;
  }
  .card--front .wordmark { left: 45px; top: 100px; width: 170px; font-size: 26px; color: var(--brand-red); text-align: center; }
  .card--back .wordmark { left: 0; right: 0; top: 100px; font-size: 36px; color: var(--white); text-align: center; }

  .divider { position: absolute; left: 231px; top: 67px; width: 1px; height: 128px; background: var(--rule); }

  .contact { position: absolute; left: 257px; top: 82px; }
  .contact__name { font-size: 18px; font-weight: 700; color: var(--brand-red); line-height: 1.1; }
  .contact__role { font-size: 13.5px; color: var(--ink); margin-top: 1px; }
  .contact__list { list-style: none; margin-top: 13px; }
  .contact__item { display: flex; align-items: center; gap: 6px; font-size: 12.5px; color: var(--muted); height: 17.5px; }
  .contact__icon { width: 12px; height: 12px; flex: none; }

  .social { position: absolute; top: 23px; right: 30px; display: flex; gap: 8px; }
  .social__link { display: flex; align-items: center; gap: 4px; font-size: 11px; font-weight: 700; color: var(--white); }
  .social__square { width: 10px; height: 10px; background: var(--white); }
</style>
</head>
<body>
<main class="canvas">

  <section class="card card--front" aria-label="Card front">
    <span class="crop-mark crop-mark--tl"></span>
    <span class="crop-mark crop-mark--tr"></span>
    <span class="crop-mark crop-mark--bl"></span>
    <span class="crop-mark crop-mark--br"></span>

    <div class="wordmark">Copperlatch<br>Pictures</div>
    <div class="divider"></div>

    <div class="contact">
      <p class="contact__name">Benedikt Harwell</p>
      <p class="contact__role">Producer/Writer/Director</p>
      <ul class="contact__list">
        <li class="contact__item">
          <svg class="contact__icon" viewBox="0 0 24 24" aria-hidden="true"><path fill="#e31b23" d="M6.6 10.8a15.1 15.1 0 0 0 6.6 6.6l2.2-2.2c.3-.3.7-.4 1-.2 1.1.4 2.3.6 3.6.6.6 0 1 .4 1 1V20c0 .6-.4 1-1 1A17 17 0 0 1 3 4c0-.6.4-1 1-1h3.5c.6 0 1 .4 1 1 0 1.3.2 2.5.6 3.6.1.3 0 .7-.2 1z"/></svg>
          555 014 2290
        </li>
        <li class="contact__item">
          <svg class="contact__icon" viewBox="0 0 24 24" aria-hidden="true"><rect x="2" y="5" width="20" height="14" fill="#e31b23"/><path d="M2 5l10 8 10-8" fill="none" stroke="#f7f7f7" stroke-width="2"/></svg>
          hello@copperlatchpictures.com
        </li>
        <li class="contact__item">
          <svg class="contact__icon" viewBox="0 0 24 24" aria-hidden="true"><circle cx="12" cy="12" r="10" fill="#e31b23"/><path d="M2 12h20M12 2c3 3 3 17 0 20M12 2c-3 3-3 17 0 20" fill="none" stroke="#f7f7f7" stroke-width="1.5"/></svg>
          www.copperlatchpictures.com
        </li>
      </ul>
    </div>
  </section>

  <section class="card card--back" aria-label="Card back">
    <span class="crop-mark crop-mark--tl"></span>
    <span class="crop-mark crop-mark--tr"></span>
    <span class="crop-mark crop-mark--bl"></span>
    <span class="crop-mark crop-mark--br"></span>

    <div class="social">
      <span class="social__link"><span class="social__square"></span>Friendloop</span>
      <span class="social__link"><span class="social__square"></span>Chirper</span>
    </div>

    <div class="wordmark">Copperlatch<br>Pictures</div>
  </section>

</main>
</body>
</html>
```